Homepage für Immobilienmakler
Zielgruppe
Wir sind ein neuer und junger Immobilienmakler. Wir wollen moderne und neue Wege gehen. Damit meinen wir, extrem modern und auffallend professionell.
Unsere Immobilien sind von Anlegerwohnungen über Häuser bis hin zu Gewerbeimmobilien
Unsere Zielgruppe ist von jung bis alt quer durch.
Aufgabenstellung
Homepagegestalltung für unsere Immobilienmaklerei.
Persönlich gefällt mir sehr gut das schwarz-weiß, jedoch wirkt das dann eher zu dunkel nehme ich mal an. Sonst würde mir die Homepage in grün, wie die Farbe im Logo, gut gefallen. Eventuell in weißer Schrift. ABER, ICH ÜBERLASSE EUCH DIE DESIGNSFARBEN.
Mir hätte dieses Design sehr gut gefallen, eventuelll könnt ihr dieses umgestallten:
http://vorlagenhain.example/item/auto-dealer-car-dealer-html-template/full_screen_preview/7719034
Kein muss, wenn ihr etwas besseres habt, dann bin ich auch froh ;)
Eventuell etwas mit Bewegung auf der Homepage oder so wäre auch gut.
Unsere Homepage hat die Domain:
wohnraum-kontor.example
Das Foto von mir sollte auf der Homepage eingebaut werden.
Auf der Homepage sollen die Immobilien, die wir verkaufen und vermieten angeführt werden. Zudem sollte ersichtlich sein, dass wir Immobilien suchen, um diese zu verkaufen oder zu vermieten.

```html
<!DOCTYPE html>
<html lang="de">
<head>
<meta charset="utf-8">
<title>Wohnraum Kontor – Immobilien</title>
<link href="https://fonts.googleapis.com/css2?family=Arimo:wght@400;700&display=swap" rel="stylesheet">
<style>
:root{
  --black:#000;
  --ink:#222;
  --white:#fff;
  --green:#8cc63f;
  --band:#e6e6e6;
  --panel:#e4e4e4;
  --rule:#c8c8c8;
  --bar:#1e1e1e;
}
*{box-sizing:border-box;margin:0;padding:0}
html,body{width:919px;height:1200px;overflow:hidden;background:var(--white)}
body{position:relative;font-family:"Arimo",Arial,sans-serif;color:var(--ink)}
.abs{position:absolute}
.header{left:0;top:0;width:919px;height:145px;background:var(--black)}
.portrait{left:72px;top:16px;width:58px;height:129px;background:linear-gradient(180deg,#6b5a4a 0%,#e8e8e8 35%,#cfcfcf 70%,#333 100%);border-radius:24px 24px 0 0}
.brand{left:148px;top:22px;font-size:48px;font-weight:700;color:var(--white);letter-spacing:-1px;white-space:nowrap}
.social{top:31px;width:14px;height:14px;background:#d8d8d8}
.nav{left:0;top:145px;width:919px;height:33px;background:var(--band)}
.nav a{position:absolute;top:9px;font-size:13px;font-weight:700;color:var(--ink);text-decoration:none}
.section-title{left:72px;font-size:19px;font-weight:700}
.rule{left:72px;width:770px;height:1px;background:var(--rule)}
.photo{background:linear-gradient(180deg,#9fb8d6 0%,#dfe6ee 40%,#e9e9e6 60%,#5c7a3a 100%)}
.photo.dusk{background:linear-gradient(180deg,#2e4e7a 0%,#6f89a8 45%,#3d3a30 75%,#2f4a2a 100%)}
.photo.sky{background:linear-gradient(180deg,#3f78c2 0%,#8fb2dc 45%,#efefef 70%,#7e8a6e 100%)}
.photo.bright{background:linear-gradient(180deg,#2f6fc4 0%,#dfe7f0 50%,#f3f3f3 75%,#7a9a55 100%)}
.caption{background:var(--bar);color:var(--white);font-size:14px;font-weight:700}
.caption span{position:absolute;top:10px}
.caption .price{color:var(--green)}
.panel{background:var(--panel);border:1px solid #cfcfcf}
.panel h2{position:absolute;left:24px;font-size:13.5px;font-weight:700;line-height:19px}
.panel p{position:absolute;left:24px;font-size:12.5px;line-height:18px;color:#333}
.panel input{position:absolute;top:36px;height:28px;background:var(--white);border:1px solid #d0d0d0}
.marker{border-radius:50%;background:var(--green)}
.arrows{left:818px;top:614px}
.footer{left:0;top:1028px;width:919px;height:172px;background:var(--band)}
.footer .col{position:absolute;top:31px;font-size:12.5px;line-height:18px;color:#333}
.footer h3{font-size:13.5px;font-weight:700;color:var(--ink);margin-bottom:12px}
</style>
</head>
<body>
<header class="abs header">
  <div class="abs portrait" role="img" aria-label="Foto des Maklers in weißem Hemd mit Mappe"></div>
  <div class="abs brand">Wohnraum Kontor</div>
  <div class="abs social" style="left:784px"></div>
  <div class="abs social" style="left:809px"></div>
  <div class="abs social" style="left:835px"></div>
</header>

<nav class="abs nav">
  <a style="left:71px">Immobilien Kaufen</a>
  <a style="left:265px">Immobilien Verkaufen</a>
  <a style="left:459px">Kontakt</a>
</nav>

<h1 class="abs section-title" style="top:218px">Aktuelle Angebote</h1>
<div class="abs rule" style="top:245px"></div>

<div class="abs photo" style="left:71px;top:269px;width:383px;height:265px" role="img" aria-label="Weißes Einfamilienhaus mit Solardach und Garten"></div>
<div class="abs caption" style="left:71px;top:534px;width:383px;height:33px"><span style="left:10px">Angebot</span><span class="price" style="right:12px">Preis</span></div>

<div class="abs panel" style="left:463px;top:269px;width:386px;height:204px">
  <h2 style="top:10px">Immobilien kaufen, mieten, verkaufen, vermieten.<br>Alles bei ihrer Wohnraum Kontor.</h2>
  <p style="top:61px">Überall dieselbe alte Leier. Das Layout ist fertig, der Text lässt<br>auf sich warten. Damit das Layout nun nicht nackt im Raume<br>steht und sich klein und leer vorkommt.</p>
  <p style="top:177px">Lesen Sie <u>hier</u> die Meinungen unserer Kunden.</p>
  <div class="abs marker" style="left:282px;top:108px;width:66px;height:66px"></div>
</div>

<div class="abs panel" style="left:463px;top:487px;width:386px;height:80px">
  <h2 style="top:12px">Hier ist Platz für den Finanzrechner.</h2>
  <input style="left:22px;width:218px" aria-label="Kaufpreis">
  <input style="left:251px;width:97px" aria-label="Laufzeit">
</div>

<h1 class="abs section-title" style="top:610px">Übersicht</h1>
<svg class="abs arrows" width="24" height="16" viewBox="0 0 24 16"><polygon points="8,0 8,16 0,8" fill="#555"/><polygon points="14,0 14,16 22,8" fill="#555"/></svg>
<div class="abs rule" style="top:637px"></div>

<!-- Übersicht Reihe 1 -->
<div class="abs photo dusk" style="left:71px;top:661px;width:187px;height:106px" role="img" aria-label="Moderne Villa mit Pool in der Dämmerung"></div>
<div class="abs caption" style="left:71px;top:767px;width:187px;height:34px"><span style="left:10px">Angebot</span><span class="price" style="right:22px">Preis</span></div>
<div class="abs photo sky" style="left:267px;top:661px;width:187px;height:106px" role="img" aria-label="Weißes kubisches Wohnhaus"></div>
<div class="abs caption" style="left:267px;top:767px;width:187px;height:34px"><span style="left:14px">Angebot</span><span class="price" style="right:17px">Preis</span></div>
<div class="abs photo bright" style="left:464px;top:661px;width:187px;height:106px" role="img" aria-label="Weißes Landhaus mit Balkonen"></div>
<div class="abs caption" style="left:464px;top:767px;width:187px;height:34px"><span style="left:14px">Angebot</span><span class="price" style="right:17px">Preis</span></div>
<div class="abs photo" style="left:661px;top:661px;width:188px;height:106px" role="img" aria-label="Einfamilienhaus mit Solardach"></div>
<div class="abs caption" style="left:661px;top:767px;width:188px;height:34px"><span style="left:12px">Angebot</span><span class="price" style="right:20px">Preis</span></div>

<!-- Übersicht Reihe 2 -->
<div class="abs photo dusk" style="left:71px;top:818px;width:187px;height:107px" role="img" aria-label="Moderne Villa mit Pool in der Dämmerung"></div>
<div class="abs caption" style="left:71px;top:925px;width:187px;height:34px"><span style="left:10px">Angebot</span><span class="price" style="right:22px">Preis</span></div>
<div class="abs photo sky" style="left:267px;top:818px;width:187px;height:107px" role="img" aria-label="Weißes kubisches Wohnhaus"></div>
<div class="abs caption" style="left:267px;top:925px;width:187px;height:34px"><span style="left:14px">Angebot</span><span class="price" style="right:17px">Preis</span></div>
<div class="abs photo bright" style="left:464px;top:818px;width:187px;height:107px" role="img" aria-label="Weißes Landhaus mit Balkonen"></div>
<div class="abs caption" style="left:464px;top:925px;width:187px;height:34px"><span style="left:14px">Angebot</span><span class="price" style="right:17px">Preis</span></div>
<div class="abs photo" style="left:661px;top:818px;width:188px;height:107px" role="img" aria-label="Einfamilienhaus mit Solardach"></div>
<div class="abs caption" style="left:661px;top:925px;width:188px;height:34px"><span style="left:12px">Angebot</span><span class="price" style="right:20px">Preis</span></div>

<footer class="abs footer">
  <div class="col" style="left:70px"><h3>Sitemap</h3>Home<br>Immobilien Kaufen<br>Immobilien Verkaufen</div>
  <div class="col" style="left:265px"><h3>Kontakt</h3>Max Mustermann<br>Musterstraße 1<br>77887 Musterstadt<br>Tel.: 01 70 00 12 34 5<br>max@beispielhaus.example</div>
  <div class="col" style="left:459px"><h3>Impressum</h3>Max Mustermann<br>Musterstraße 1<br>77887 Musterstadt<br>Tel.: 01 70 00 12 34 5</div>
  <div class="col" style="left:653px"><h3>AGB</h3></div>
  <div class="abs marker" style="left:783px;top:20px;width:66px;height:66px"></div>
</footer>
</body>
</html>
```